Coffee bag stamp design for new coffee brand

Stamp design that will be used like a label on a coffee package.
It must be a vector that can be produced as a stamp. Coffee bag is from brown craft paper. I upload image of this bag. Size of design is 80mm x 140mm.
I also uploaded two pictures for inspiration, but I will also appreciate new ideas.

Target Market(s)

Coffee lovers, who love to try new coffee. Also hipsters.

Colors

Designer to choose only greyscale colors for use in the design.

Requirements
Must have
• Some information about coffee must have:
Name: BRAZIL (the biggest font in that design)
Region: Santos
Altitude: 60 – 1200 m.n.m.
Variety: Arabica
Processing: unwashed

```html
<!DOCTYPE html>
<html lang="en">
<head>
<meta charset="utf-8">
<title>Kalmora Coffee – Brazil Santos Label</title>
<link rel="stylesheet" href="https://fonts.googleapis.com/css2?family=Alfa+Slab+One&family=Montserrat:wght@600;800&display=swap">
<style>
  :root {
    --ink: #1a1a1a;
    --paper: #ffffff;
    --line: 5px;
  }
  * { box-sizing: border-box; margin: 0; padding: 0; }
  html, body {
    width: 686px;
    height: 1200px;
    overflow: hidden;
    background: var(--paper);
  }
  .label {
    position: relative;
    width: 686px;
    height: 1200px;
    color: var(--ink);
    font-family: "Montserrat", sans-serif;
  }
  .label-frame {
    position: absolute;
    inset: 0;
  }
  .brand {
    position: absolute;
    left: 0;
    right: 0;
    top: 200px;
    text-align: center;
  }
  .brand-dot {
    display: block;
    width: 60px;
    height: 60px;
    margin: 0 auto 36px;
    border-radius: 50%;
    background: var(--ink);
  }
  .brand-name {
    font-weight: 800;
    font-size: 88px;
    line-height: 1;
    letter-spacing: 1px;
  }
  .brand-sub {
    font-weight: 800;
    font-size: 58px;
    line-height: 1.1;
    letter-spacing: 2px;
  }
  .origin {
    position: absolute;
    left: 0;
    right: 0;
    top: 655px;
    text-align: center;
    font-family: "Alfa Slab One", serif;
    font-size: 92px;
    line-height: 1;
    letter-spacing: 4px;
  }
  .specs {
    position: absolute;
    left: 73px;
    top: 776px;
    width: 541px;
    height: 368px;
    border: var(--line) solid var(--ink);
    display: grid;
    grid-template-rows: 112px 92px 91px 1fr;
  }
  .region {
    position: absolute;
    left: 50%;
    top: -24px;
    transform: translateX(-50%);
    padding: 0 16px;
    background: var(--paper);
    font-weight: 600;
    font-size: 36px;
    line-height: 44px;
    letter-spacing: 1px;
  }
  .spec-row {
    display: flex;
    align-items: center;
    justify-content: center;
    gap: 14px;
    font-weight: 600;
    font-size: 25px;
    letter-spacing: 0.5px;
    border-bottom: var(--line) solid var(--ink);
  }
  .spec-row--first { padding-top: 20px; }
  .spec-unit { font-size: 17px; }
  .hashtag {
    display: flex;
    align-items: center;
    justify-content: center;
    background: var(--ink);
    color: var(--paper);
    font-weight: 800;
    font-size: 25px;
    letter-spacing: 0.5px;
  }
</style>
</head>
<body>
  <main class="label">
    <svg class="label-frame" width="686" height="1200" viewBox="0 0 686 1200" aria-hidden="true">
      <path d="M29,1178 V336 A314,314 0 0 1 657,336 V1178 Z" fill="none" stroke="var(--ink)" stroke-width="5"/>
    </svg>

    <header class="brand">
      <span class="brand-dot"></span>
      <div class="brand-name">KALMORA</div>
      <div class="brand-sub">COFFEE</div>
    </header>

    <h1 class="origin">BRAZIL</h1>

    <section class="specs">
      <span class="region">SANTOS</span>
      <div class="spec-row spec-row--first">ALTITUDE: <span>60 – 120 <span class="spec-unit">M.N.M.</span></span></div>
      <div class="spec-row">VARIETY: <span>100% ARABICA</span></div>
      <div class="spec-row">PROCESSING: <span>UNWASHED</span></div>
      <div class="hashtag">#KALMORACOFFEE</div>
    </section>
  </main>
</body>
</html>
```